RivoPlex PowerPoint Template with existing Logo and Letterhead template

Develop a PowerPoint template based on existing logo and letterhead designs for a Marketing Consultancy.
Presentations that will be made with title slide, content slides (which includes mostly bullet point text and some tables) and also last page company introduction and copyright.
Corporate colors should be keep as per the logo

I like something like from Artisan Hive
- Serious, Modern PowerPoint Design for Company in Canada | Design 418674
- Professional, Modern PowerPoint Design for Company in United States | Design 7795293
- Professional, Modern PowerPoint Design for Company in United States | Design 7826742
- Serious, Modern PowerPoint Design for Company in Canada | Design 418635
- Elegant, Serious PowerPoint Design for Company in Puerto Rico | Design 16951178
- Bold, Modern PowerPoint Design for Company in United States | Design 11745238

To all designers, • We need sleek and modern looking PowerPoint presentation template. • The template will primarily be used for our corporate slide and solutions presentation for our customers. • Not too much of white and it should be sleek, modern and impressive for marketing consultancy firms like us. • Please ensure the content pages are water marketed with the 4 boxes. • I like something like from Artisan Hive and you can get some idea on what I like.: o Serious, Modern PowerPoint Design for Company in Canada | Design 418674 o Professional, Modern PowerPoint Design for Company in United States | Design 7795293 o Professional, Modern PowerPoint Design for Company in United States | Design 7826742 o Serious, Modern PowerPoint Design for Company in Canada | Design 418635 o Elegant, Serious PowerPoint Design for Company in Puerto Rico | Design 16951178 o Bold, Modern PowerPoint Design for Company in United States | Design 11745238 Thanks!

Target Market(s)

Marketing Managers, B2B Marketing Team, CRM Data Owners

Industry/Entity Type

Marketing

Requirements
Must have
• Not too much of white and it should be sleek, modern and impressive for marketing consultancy firms like us. Please ensure the content pages are water marketed with the 4 boxes. The template will primarily be used for our corporate slides and solutions presentation for our customers.
Should not have
• no background in the slide content area

```html
<!DOCTYPE html>
<html lang="en">
<head>
<meta charset="utf-8">
<title>RivoPlex Presentation Template</title>
<link href="https://fonts.googleapis.com/css2?family=Source+Sans+3:wght@400;600;700&display=swap" rel="stylesheet">
<style>
:root{
  --red:#ec1c24;
  --slate:#4d5568;
  --ink:#3a3a3a;
  --muted:#9a9a9a;
  --line:#e4e4e4;
  --ghost:#f3f3f5;
  --ghost-red:#fdf0f0;
  --board:#ffffff;
  --frame:#e2e2e2;
}
*{box-sizing:border-box;margin:0;padding:0}
html,body{width:1200px;height:1072px;overflow:hidden;background:var(--board);font-family:"Source Sans 3",sans-serif;color:var(--ink)}
.board{position:relative;width:1200px;height:1072px}
.brand-head{position:absolute;left:0;right:0;top:44px;text-align:center}
.brand-name{font-weight:700;font-size:34px;color:var(--red);letter-spacing:1px}
.brand-name .mark{display:inline-block;width:9px;height:9px;background:var(--red);margin-left:4px;vertical-align:top}
.slide{position:absolute;width:381px;height:213px;background:#fff;box-shadow:0 0 0 1px var(--frame),0 1px 4px rgba(0,0,0,.12);overflow:hidden}
.c1{left:18px}.c2{left:410px}.c3{left:802px}
.r1{top:142px}.r2{top:374px}.r3{top:606px}.r4{top:838px}
.logo{position:absolute;font-weight:700;color:var(--red);white-space:nowrap}
.logo-lg{font-size:13px;left:28px;top:52px}
.logo-sm{font-size:7px;right:24px;top:23px}
.ghost{position:absolute;background:var(--ghost)}
.ghost.red{background:var(--ghost-red)}
.pres-title{position:absolute;left:28px;top:84px;font-size:19px;font-weight:700;color:var(--red)}
.pres-sub{position:absolute;left:28px;top:109px;font-size:7px;font-weight:600;color:var(--slate)}
.speaker{position:absolute;left:28px;top:144px;font-size:8px;font-weight:600;color:var(--red)}
.job{position:absolute;left:28px;top:156px;font-size:4px;color:var(--ink)}
.wave{position:absolute;left:0;bottom:0;width:381px;height:50px}
.city{position:absolute;right:0;top:0;width:230px;height:213px;background:linear-gradient(90deg,rgba(255,255,255,1) 0%,rgba(230,232,236,.7) 35%,#c9ced6 70%,#d6d9df 100%)}
.topic{position:absolute;left:18px;top:16px;font-size:4px;color:var(--muted)}
.s-title{position:absolute;left:18px;top:21px;font-size:11px;font-weight:600;color:var(--red)}
.pg{position:absolute;right:4px;bottom:6px;width:14px;height:7px;background:var(--ghost);font-size:3px;text-align:center;line-height:7px;color:var(--muted)}
.body{position:absolute;font-size:5px;line-height:1.55;color:var(--ink)}
.body p{margin-bottom:4px}
.bullets{left:18px;top:50px;width:345px;list-style:none}
.bullets li{position:relative;padding-left:8px;margin-bottom:6px}
.bullets li::before{content:"›";position:absolute;left:0;color:var(--slate)}
.cols{top:52px;display:flex;gap:12px;left:18px;width:345px}
.cols div{flex:1}
table{border-collapse:collapse}
.opt{position:absolute;left:16px;top:56px;width:350px;font-size:4.5px}
.opt th{background:var(--red);color:#fff;height:15px;font-weight:600}
.opt td{height:18.5px;text-align:center;color:var(--muted);border-bottom:1px solid #f0f0f0}
.opt td:first-child{text-align:left;padding-left:10px}
.feat{position:absolute;left:24px;top:54px;width:330px}
.feat-row{display:flex;align-items:center;height:27px}
.tick{width:14px;height:14px;margin-right:10px;flex:none}
.feat-row b{display:block;font-size:5.5px;font-weight:600;color:var(--ink)}
.feat-row span{display:block;font-size:4px;color:#b6b6b6}
.steps{position:absolute;left:26px;top:62px}
.step-txt{position:absolute;font-size:4.3px;line-height:1.35;width:40px;color:var(--ink)}
.step-txt b{display:block;font-size:6px;margin-bottom:4px;font-weight:600}
.step-txt.on-red b{color:var(--red)}
.fin-cap{position:absolute;left:32px;top:55px;font-size:6px;color:var(--ink)}
.fin{position:absolute;left:30px;top:66px;width:322px;font-size:4.6px}
.fin th{background:var(--red);color:#fff;height:12px;font-weight:700}
.fin th:first-child{background:#fff}
.fin td{height:10.8px;text-align:center;border-bottom:1px solid var(--line);border-left:1px solid var(--line)}
.fin td:first-child{text-align:left;padding-left:2px;border-left:0;width:66px}
.fin tr.total td{background:#e6e6e6;font-weight:700}
.months{position:absolute;left:26px;top:56px;width:340px;display:grid;grid-template-columns:repeat(4,1fr);row-gap:10px;column-gap:8px}
.pill{display:inline-block;background:var(--red);color:#fff;font-size:4px;font-weight:700;padding:2px 8px;border-radius:8px}
.m-title{font-size:6px;color:var(--red);margin:5px 0 3px}
.m-body{font-size:4.2px;line-height:1.45}
.monitor{position:absolute;left:208px;top:64px;width:142px;height:120px}
.screen{position:absolute;left:3px;top:3px;width:136px;height:75px;background:linear-gradient(180deg,#b9c7d3 0%,#7e8f8c 55%,#4f5c55 100%)}
.thanks-panel{position:absolute;left:0;top:0;width:167px;height:213px;background:#f7f7f8}
.thanks{position:absolute;left:0;width:167px;text-align:center;top:88px;font-size:19px;font-weight:700;color:var(--red)}
.thanks-sub{position:absolute;left:0;width:167px;text-align:center;top:112px;font-size:6px;font-weight:600;color:var(--slate)}
.contact{position:absolute;left:56px;top:134px;font-size:5.5px;line-height:2.3;color:var(--slate)}
.contact b{color:var(--red);margin-right:4px}
.copy{position:absolute;left:0;width:167px;text-align:center;bottom:6px;font-size:3px;color:var(--muted)}
.sq{position:absolute}
</style>
</head>
<body>
<div class="board">

<header class="brand-head"><span class="brand-name">RivoPlex<span class="mark"></span></span></header>

<!-- Title slide -->
<section class="slide c1 r1">
  <div class="ghost red" style="left:267px;top:26px;width:32px;height:32px"></div>
  <div class="ghost" style="left:318px;top:66px;width:38px;height:38px"></div>
  <div class="ghost" style="left:244px;top:86px;width:46px;height:46px"></div>
  <div class="ghost red" style="left:306px;top:130px;width:64px;height:52px"></div>
  <div class="logo logo-lg">RivoPlex</div>
  <h1 class="pres-title">Presentation title</h1>
  <div class="pres-sub">Subtitle here</div>
  <div class="speaker">Speaker name</div>
  <div class="job">Job title here</div>
  <svg class="wave" viewBox="0 0 381 50" preserveAspectRatio="none">
    <path d="M0 50 L0 20 C90 4 200 40 381 16 L381 50 Z" fill="var(--red)"/>
    <path d="M0 12 C90 -2 200 30 381 6 L381 11 C200 36 90 4 0 18 Z" fill="var(--slate)"/>
  </svg>
</section>

<!-- Title slide with photo -->
<section class="slide c2 r1">
  <div class="city" role="img" aria-label="Faded city skyline photograph"></div>
  <div class="logo logo-lg">RivoPlex</div>
  <h1 class="pres-title">Presentation title</h1>
  <div class="pres-sub">Subtitle here</div>
  <div class="speaker">Speaker name</div>
  <div class="job">Job title here</div>
</section>

<!-- Bullet slide -->
<section class="slide c3 r1">
  <div class="topic">Main topic here</div>
  <h2 class="s-title">Slide title here</h2>
  <div class="logo logo-sm">RivoPlex</div>
  <ul class="body bullets">
    <li>Lorem ipsum dolor sit amet, nam graece verear aperiam ut. Duo cu alii definitionem, magna accumsan quo at. Id quo illum option mediocritatem, et illud simul nam, at vel nibh docendi posidonium. Mei ei tation evertitur.</li>
    <li>Cum et probo sadipscing, in duo illum pertinacia. Sea ea ullum sapientem. Aeque interpretaris et pro, nec lucilius repudiandae id. Vim ea nobis vitae, id nisl melius ius. Ne wisi persecuti his.</li>
    <li>Per vero vidit disputando an, no case reprimique eam, et tritani accommodare vim. Ut vis mandamus reformidans, vidit latine neglegentur at cum. Ut malis error eam. His eu quot verear, facilis voluptaria eu mea.</li>
    <li>Cum tempor integre honestatis in, et sit hinc graeco vocibus. Has id graecis appetere mnesarchum. Ei error convenire iracundia cum, nec ne putant utroque. Cum id quem liberavisse theophrastus.</li>
    <li>Et mel congue vidisse. Id ubique impedit argumentum pri, ne ignota nostrum cum. Legimus accusata patrioque eu mel, ei vel alia placerat, quo harum cetero dignissim an. Cum no augue choro.</li>
  </ul>
  <div class="pg">1</div>
</section>

<!-- Two columns -->
<section class="slide c1 r2">
  <div class="topic">Main topic here</div>
  <h2 class="s-title">Slide title here</h2>
  <div class="logo logo-sm">RivoPlex</div>
  <div class="body cols">
    <div><p>Lorem ipsum dolor sit amet, nam graece verear aperiam ut. Duo cu alii definitionem, magna accumsan quo at. Id quo illum option mediocritatem, et illud simul nam, at vel nibh docendi posidonium. Mei ei tation evertitur.</p><p>Cum et probo sadipscing, in duo illum pertinacia. Sea ea ullum sapientem. Aeque interpretaris et pro, nec lucilius repudiandae id. Vim ea nobis vitae, id nisl melius ius. Ne wisi persecuti his. Justo erant movet cu eam.</p><p>Per vero vidit disputando an, no case reprimique eam, et tritani accommodare vim. Ut vis mandamus reformidans, vidit latine neglegentur at cum. Ut malis error eam.</p></div>
    <div><p>Cum tempor integre honestatis in, et sit hinc graeco vocibus. Has id graecis appetere mnesarchum. Ei error convenire iracundia cum, nec ne putant utroque. Cum id quem liberavisse theophrastus, at unum nostrud aliquando eam.</p><p>Et mel congue vidisse. Id ubique impedit argumentum pri, ne ignota nostrum cum. Legimus accusata patrioque eu mel, ei vel alia placerat, quo harum cetero dignissim an. Cum no augue choro, has clita ceteros tibique no.</p></div>
  </div>
  <div class="pg">1</div>
</section>

<!-- Three columns -->
<section class="slide c2 r2">
  <div class="topic">Main topic here</div>
  <h2 class="s-title">Slide title here</h2>
  <div class="logo logo-sm">RivoPlex</div>
  <div class="body cols">
    <div><p>Lorem ipsum dolor sit amet, nam graece verear aperiam ut. Duo cu alii definitionem, magna accumsan quo at. Id quo illum option mediocritatem, et illud simul nam.</p><p>Cum et probo sadipscing, in duo illum pertinacia. Sea ea ullum sapientem. Aeque interpretaris et pro, nec lucilius repudiandae id. Justo erant movet cu eam.</p><p>Per vero vidit disputando an, no case reprimique eam, et tritani accommodare vim.</p></div>
    <div><p>Latine neglegentur at cum. Ut malis error eam. His eu quot verear, facilis voluptaria eu mea. Vix vide fugit omittantur et. Has ut habeo volumus argumentum.</p><p>Cum tempor integre honestatis in, et sit hinc graeco vocibus. Has id graecis appetere mnesarchum. Ei error convenire iracundia cum, nec ne putant utroque.</p></div>
    <div><p>Sensibus deterruisset.</p><p>Et mel congue vidisse. Id ubique impedit argumentum pri, ne ignota nostrum cum. Legimus accusata patrioque eu mel, ei vel alia placerat, quo harum cetero dignissim an. Cum no augue choro.</p></div>
  </div>
  <div class="pg">1</div>
</section>

<!-- Options table -->
<section class="slide c3 r2">
  <div class="topic">Main topic here</div>
  <h2 class="s-title">Slide title here</h2>
  <div class="logo logo-sm">RivoPlex</div>
  <table class="opt">
    <tr><th></th><th>Option 01</th><th>Option 02</th><th>Option 03</th><th>Option 04</th><th>Option 05</th><th>Option 06</th><th>Option 07</th></tr>
    <tr><td>Option 01</td><td>$32,500</td><td>$32,500</td><td>$32,500</td><td>$32,500</td><td>$32,500</td><td>$32,500</td><td>$32,500</td></tr>
    <tr><td>Option 02</td><td>$32,500</td><td>$32,500</td><td>$32,500</td><td>$32,500</td><td>$32,500</td><td>$32,500</td><td>$32,500</td></tr>
    <tr><td>Option 03</td><td>$32,500</td><td>$32,500</td><td>$32,500</td><td>$32,500</td><td>$32,500</td><td>$32,500</td><td>$32,500</td></tr>
    <tr><td>Option 04</td><td>$32,500</td><td>$32,500</td><td>$32,500</td><td>$32,500</td><td>$32,500</td><td>$32,500</td><td>$32,500</td></tr>
    <tr><td>Option 05</td><td>$32,500</td><td>$32,500</td><td>$32,500</td><td>$32,500</td><td>$32,500</td><td>$32,500</td><td>$32,500</td></tr>
    <tr><td>Option 06</td><td>$32,500</td><td>$32,500</td><td>$32,500</td><td>$32,500</td><td>$32,500</td><td>$32,500</td><td>$32,500</td></tr>
  </table>
  <div class="pg">1</div>
</section>

<!-- Features -->
<section class="slide c1 r3">
  <div class="topic">Main topic here</div>
  <h2 class="s-title">Slide title here</h2>
  <div class="logo logo-sm">RivoPlex</div>
  <div class="feat">
    <div class="feat-row"><svg class="tick" viewBox="0 0 14 14"><circle cx="7" cy="7" r="6.3" fill="none" stroke="var(--red)" stroke-width=".9"/><path d="M4 7.2l2 2 4-4.2" fill="none" stroke="var(--red)" stroke-width=".9"/></svg><div><b>Feature #1</b><span>Lorem ipsum dolor sit amet, ex paulo vidisse eos. Nec ut persius admodum civibus, an hinc iudico principes sea.</span></div></div>
    <div class="feat-row"><svg class="tick" viewBox="0 0 14 14"><circle cx="7" cy="7" r="6.3" fill="none" stroke="var(--red)" stroke-width=".9"/><path d="M4 7.2l2 2 4-4.2" fill="none" stroke="var(--red)" stroke-width=".9"/></svg><div><b>Feature #2</b><span>Lorem ipsum dolor sit amet, ex paulo vidisse eos. Nec ut persius admodum civibus, an hinc iudico principes sea.</span></div></div>
    <div class="feat-row"><svg class="tick" viewBox="0 0 14 14"><circle cx="7" cy="7" r="6.3" fill="none" stroke="var(--red)" stroke-width=".9"/><path d="M4 7.2l2 2 4-4.2" fill="none" stroke="var(--red)" stroke-width=".9"/></svg><div><b>Feature #3</b><span>Lorem ipsum dolor sit amet, ex paulo vidisse eos. Nec ut persius admodum civibus, an hinc iudico principes sea.</span></div></div>
    <div class="feat-row"><svg class="tick" viewBox="0 0 14 14"><circle cx="7" cy="7" r="6.3" fill="none" stroke="var(--red)" stroke-width=".9"/><path d="M4 7.2l2 2 4-4.2" fill="none" stroke="var(--red)" stroke-width=".9"/></svg><div><b>Feature #4</b><span>Lorem ipsum dolor sit amet, ex paulo vidisse eos. Nec ut persius admodum civibus, an hinc iudico principes sea.</span></div></div>
    <div class="feat-row"><svg class="tick" viewBox="0 0 14 14"><circle cx="7" cy="7" r="6.3" fill="none" stroke="var(--red)" stroke-width=".9"/><path d="M4 7.2l2 2 4-4.2" fill="none" stroke="var(--red)" stroke-width=".9"/></svg><div><b>Feature #5</b><span>Lorem ipsum dolor sit amet, ex paulo vidisse eos. Nec ut persius admodum civibus, an hinc iudico principes sea.</span></div></div>
  </div>
  <div class="pg">1</div>
</section>

<!-- Process steps -->
<section class="slide c2 r3">
  <div class="topic">Main topic here</div>
  <h2 class="s-title">Slide title here</h2>
  <div class="logo logo-sm">RivoPlex</div>
  <svg class="steps" width="336" height="96" viewBox="0 0 336 96">
    <defs>
      <path id="chev" d="M0 0 H52 L84 48 L52 96 H0 L32 48 Z"/>
    </defs>
    <g>
      <path d="M2 4 H50 L78 48 L50 92 H2 Z" fill="#fff"/>
      <path d="M0 0 H56 L88 48 L56 96 H0 V92 H50 Q60 92 70 74 L80 48 L70 22 Q60 4 50 4 H0 Z" fill="var(--red)"/>
    </g>
    <g transform="translate(81 0)">
      <path d="M0 0 H56 L88 48 L56 96 H0 V92 H50 Q60 92 70 74 L80 48 L70 22 Q60 4 50 4 H0 Z" fill="var(--slate)"/>
    </g>
    <g transform="translate(162 0)">
      <path d="M0 0 H56 L88 48 L56 96 H0 V92 H50 Q60 92 70 74 L80 48 L70 22 Q60 4 50 4 H0 Z" fill="var(--red)"/>
    </g>
    <g transform="translate(243 0)">
      <path d="M0 0 H56 L88 48 L56 96 H0 V92 H50 Q60 92 70 74 L80 48 L70 22 Q60 4 50 4 H0 Z" fill="var(--slate)"/>
    </g>
  </svg>
  <div class="step-txt on-red" style="left:37px;top:94px"><b>Step 1</b>Lorem ipsum dolor sit amet, consectetur adipisicied do dolore magna aliqua.</div>
  <div class="step-txt" style="left:118px;top:94px"><b>Step 2</b>Lorem ipsum dolor sit amet, consectetur adipisicied do dolore magna aliqua.</div>
  <div class="step-txt on-red" style="left:199px;top:94px"><b>Step 3</b>Lorem ipsum dolor sit amet, consectetur adipisicied do dolore magna aliqua.</div>
  <div class="step-txt" style="left:280px;top:94px"><b>Step 4</b>Lorem ipsum dolor sit amet, consectetur adipisicied do dolore magna aliqua.</div>
  <div class="pg">1</div>
</section>

<!-- Financials -->
<section class="slide c3 r3">
  <div class="topic">Main topic here</div>
  <h2 class="s-title">Slide title here</h2>
  <div class="logo logo-sm">RivoPlex</div>
  <div class="fin-cap">Financials (billions)</div>
  <table class="fin">
    <tr><th></th><th>2010</th><th>2011</th><th>2012</th><th>2013</th><th>2014</th><th>2015</th></tr>
    <tr><td>Revenue</td><td>15.6</td><td>17.1</td><td>15.6</td><td>17.1</td><td>15.6</td><td>17.1</td></tr>
    <tr><td>Cost of Revenue</td><td>10.6</td><td>10.8</td><td>10.6</td><td>10.8</td><td>10.6</td><td>10.8</td></tr>
    <tr><td>Gross Profit</td><td>5.0</td><td>6.3</td><td>5.0</td><td>6.3</td><td>5.0</td><td>6.3</td></tr>
    <tr><td>R&amp;D</td><td>0.48</td><td>0.49</td><td>0.48</td><td>0.49</td><td>0.48</td><td>0.49</td></tr>
    <tr><td>General/Sales</td><td>1.1</td><td>1.0</td><td>1.1</td><td>1.0</td><td>1.1</td><td>1.0</td></tr>
    <tr><td>EBITDA</td><td>3.4</td><td>4.8</td><td>3.4</td><td>4.8</td><td>3.4</td><td>4.8</td></tr>
    <tr><td>Tax</td><td>1.3</td><td>1.9</td><td>1.3</td><td>1.9</td><td>1.3</td><td>1.9</td></tr>
    <tr><td>Interest Expense</td><td>–</td><td>–</td><td>–</td><td>–</td><td>–</td><td>–</td></tr>
    <tr class="total"><td>Net Income</td><td>2.1</td><td>2.9</td><td>2.1</td><td>2.9</td><td>2.1</td><td>2.9</td></tr>
  </table>
  <div class="pg">1</div>
</section>

<!-- Timeline -->
<section class="slide c1 r4">
  <div class="topic">Main topic here</div>
  <h2 class="s-title">Slide title here</h2>
  <div class="logo logo-sm">RivoPlex</div>
  <div class="months">
    <div><span class="pill">JAN</span><div class="m-title">Title text demo</div><div class="m-body">Lorem ipsum dolor sit amet, consectetur adipiscing elit, incididunt ut labore et dolore magna veniam, quis nostrud</div></div>
    <div><span class="pill">FEB</span><div class="m-title">Title text demo</div><div class="m-body">Lorem ipsum dolor sit amet, consectetur adipiscing elit, incididunt ut labore et dolore magna veniam, quis nostrud</div></div>
    <div><span class="pill">MAY</span><div class="m-title">Title text demo</div><div class="m-body">Lorem ipsum dolor sit amet, consectetur adipiscing elit, incididunt ut labore et dolore magna veniam, quis nostrud</div></div>
    <div><span class="pill">JUN</span><div class="m-title">Title text demo</div><div class="m-body">Lorem ipsum dolor sit amet, consectetur adipiscing elit, incididunt ut labore et dolore magna veniam, quis nostrud</div></div>
    <div><span class="pill">JUL</span><div class="m-title">Title text demo</div><div class="m-body">Lorem ipsum dolor sit amet, consectetur adipiscing elit, incididunt ut labore et dolore magna veniam, quis nostrud</div></div>
    <div><span class="pill">AUG</span><div class="m-title">Title text demo</div><div class="m-body">Lorem ipsum dolor sit amet, consectetur adipiscing elit, incididunt ut labore et dolore magna veniam, quis nostrud</div></div>
    <div><span class="pill">SEP</span><div class="m-title">Title text demo</div><div class="m-body">Lorem ipsum dolor sit amet, consectetur adipiscing elit, incididunt ut labore et dolore magna veniam, quis nostrud</div></div>
    <div><span class="pill">NOV</span><div class="m-title">Title text demo</div><div class="m-body">Lorem ipsum dolor sit amet, consectetur adipiscing elit, incididunt ut labore et dolore magna veniam, quis nostrud</div></div>
  </div>
  <div class="pg">1</div>
</section>

<!-- Text with monitor -->
<section class="slide c2 r4">
  <div class="topic">Main topic here</div>
  <h2 class="s-title">Slide title here</h2>
  <div class="logo logo-sm">RivoPlex</div>
  <div class="body" style="left:26px;top:70px;width:160px;line-height:1.7">
    <p>Lorem ipsum dolor sit amet, nam graece verear aperiam ut. Duo cu alii definitionem, magna accumsan quo at. Id quo illum option mediocritatem, et illud simul nam, at vel nibh docendi posidonium. Mei ei tation evertitur.</p>
    <p>Cum et probo sadipscing, in duo illum pertinacia. Sea ea ullum sapientem. Aeque interpretaris et pro, nec lucilius repudiandae id. Vim ea nobis vitae, id nisl melius ius. Ne wisi persecuti his. Justo erant movet cu eam.</p>
  </div>
  <div class="monitor">
    <svg width="142" height="120" viewBox="0 0 142 120">
      <rect x="0" y="0" width="142" height="84" rx="2" fill="#2b2b2b"/>
      <rect x="0" y="84" width="142" height="10" fill="#e6e6e6"/>
      <path d="M58 94 H84 L88 110 H54 Z" fill="#d4d4d4"/>
      <rect x="48" y="110" width="46" height="3" rx="1.5" fill="#c4c4c4"/>
    </svg>
    <div class="screen" role="img" aria-label="City skyline photograph on screen"></div>
  </div>
  <div class="pg">1</div>
</section>

<!-- Thank you -->
<section class="slide c3 r4">
  <div class="thanks-panel"></div>
  <div class="logo" style="font-size:12px;left:0;width:167px;text-align:center;top:52px">RivoPlex</div>
  <div class="thanks">THANK YOU</div>
  <div class="thanks-sub">FEEL FREE TO CONTACT US!</div>
  <div class="contact">
    <div><b>t:</b>+12 34 33 1233</div>
    <div><b>e:</b>email@domain.com</div>
    <div><b>w:</b>domain.com</div>
  </div>
  <div class="copy">Eu cum wisi nobis, aimed neglegentur est te. Ve mea posse vocibus id, te est perpetua scriptorem.</div>
  <div class="sq" style="left:247px;top:27px;width:32px;height:32px;background:var(--red)"></div>
  <div class="sq" style="left:298px;top:67px;width:38px;height:38px;background:var(--slate)"></div>
  <div class="sq" style="left:224px;top:86px;width:46px;height:46px;background:var(--slate)"></div>
  <div class="sq" style="left:286px;top:130px;width:65px;height:65px;background:var(--red)"></div>
</section>

</div>
</body>
</html>
```